Business Card Design Project

I have attached the logo and the colour pallete for the branding for the company.

Creative designs for business cards are needed.

The Company is modern corporate.

Industry/Entity Type

Business

```html
<!DOCTYPE html>
<html lang="en">
<head>
<meta charset="utf-8">
<title>Gulfwise Business Card</title>
<link href="https://fonts.googleapis.com/css2?family=PT+Sans:wght@400;700&display=swap" rel="stylesheet">
<style>
  :root {
    --page: #e8e4de;
    --card: #f7f1e6;
    --purple: #6a2b6e;
    --orange: #f28c22;
    --red: #e4283f;
    --ink: #3b3436;
    --rule: #7a6f6a;
  }
  * { box-sizing: border-box; margin: 0; padding: 0; }
  html, body {
    width: 1200px;
    height: 833px;
    overflow: hidden;
    background: var(--page);
    font-family: "PT Sans", sans-serif;
  }
  .card {
    position: absolute;
    left: 50px;
    top: 102px;
    width: 1100px;
    height: 629px;
    background: var(--card);
    box-shadow: 0 6px 24px rgba(0,0,0,0.12);
    overflow: hidden;
  }
  .brand-name {
    position: absolute;
    left: 0;
    top: 60px;
    width: 100%;
    text-align: center;
    font-size: 150px;
    font-weight: 700;
    letter-spacing: -2px;
    color: var(--purple);
    line-height: 1;
  }
  .identity {
    position: absolute;
    right: 608px;
    top: 330px;
    text-align: right;
  }
  .identity .person-name {
    font-size: 33px;
    font-weight: 700;
    color: var(--purple);
    line-height: 40px;
  }
  .identity .person-title {
    font-size: 25px;
    color: var(--orange);
    line-height: 32px;
  }
  .identity .address {
    margin-top: 22px;
    font-size: 27px;
    color: var(--ink);
    line-height: 38px;
  }
  .divider {
    position: absolute;
    left: 520px;
    top: 327px;
    width: 2px;
    height: 196px;
    background: var(--rule);
  }
  .contacts {
    position: absolute;
    left: 540px;
    top: 334px;
    list-style: none;
  }
  .contacts li {
    display: flex;
    align-items: center;
    height: 46.5px;
    font-size: 28px;
    color: var(--ink);
  }
  .contacts svg {
    width: 24px;
    height: 24px;
    margin-right: 10px;
    fill: var(--ink);
    flex: none;
  }
  .accent-band {
    position: absolute;
    left: 0;
    bottom: 0;
    width: 1100px;
    height: 32px;
  }
</style>
</head>
<body>
  <div class="card">
    <div class="brand-name">gulfwise</div>

    <div class="identity">
      <div class="person-name">Your Name</div>
      <div class="person-title">Title</div>
      <div class="address">Street Name, City Name<br>State Zip Code</div>
    </div>

    <div class="divider"></div>

    <ul class="contacts">
      <li>
        <svg viewBox="0 0 24 24" aria-hidden="true"><path d="M6.6 10.8a15.1 15.1 0 0 0 6.6 6.6l2.2-2.2c.3-.3.7-.4 1-.2 1.1.4 2.3.6 3.6.6.6 0 1 .4 1 1V20c0 .6-.4 1-1 1A17 17 0 0 1 3 4c0-.6.4-1 1-1h3.5c.6 0 1 .4 1 1 0 1.3.2 2.5.6 3.6.1.3 0 .7-.2 1z"/></svg>
        123-456-0789
      </li>
      <li>
        <svg viewBox="0 0 24 24" aria-hidden="true"><path d="M8 1h8a2 2 0 0 1 2 2v18a2 2 0 0 1-2 2H8a2 2 0 0 1-2-2V3a2 2 0 0 1 2-2zm0 3v12h8V4zm4 14.2a1.3 1.3 0 1 0 0 2.6 1.3 1.3 0 0 0 0-2.6z"/></svg>
        123-456-0789
      </li>
      <li>
        <svg viewBox="0 0 24 24" aria-hidden="true"><path d="M2 6a2 2 0 0 1 2-2h16a2 2 0 0 1 2 2v12a2 2 0 0 1-2 2H4a2 2 0 0 1-2-2zm2 .5V7l8 5 8-5v-.5z"/></svg>
        info@gulfwise.com
      </li>
      <li>
        <svg viewBox="0 0 24 24" aria-hidden="true"><path d="M12 2a10 10 0 1 0 0 20 10 10 0 0 0 0-20zm6.9 6h-3a15 15 0 0 0-1.3-3.9A8 8 0 0 1 18.9 8zM12 4c.8 1.1 1.5 2.5 1.9 4h-3.8c.4-1.5 1.1-2.9 1.9-4zM4.3 14a8 8 0 0 1 0-4h3.4a16 16 0 0 0 0 4zm.8 2h3a15 15 0 0 0 1.3 3.9A8 8 0 0 1 5.1 16zm3-8h-3a8 8 0 0 1 4.3-3.9A15 15 0 0 0 8.1 8zM12 20c-.8-1.1-1.5-2.5-1.9-4h3.8c-.4 1.5-1.1 2.9-1.9 4zm2.3-6H9.7a14 14 0 0 1 0-4h4.6a14 14 0 0 1 0 4zm.3 5.9a15 15 0 0 0 1.3-3.9h3a8 8 0 0 1-4.3 3.9zm1.7-5.9a16 16 0 0 0 0-4h3.4a8 8 0 0 1 0 4z"/></svg>
        www.gulfwise.com
      </li>
    </ul>

    <svg class="accent-band" viewBox="0 0 1100 32" preserveAspectRatio="none" aria-hidden="true">
      <defs>
        <linearGradient id="warm-band" x1="0" y1="0" x2="1" y2="0">
          <stop offset="0" stop-color="var(--red)" style="stop-color: var(--red)"/>
          <stop offset="1" stop-color="var(--orange)" style="stop-color: var(--orange)"/>
        </linearGradient>
      </defs>
      <polygon points="0,0 505,0 469,32 0,32" fill="url(#warm-band)"/>
      <polygon points="515,0 1100,0 1100,32 480,32" style="fill: var(--purple)"/>
    </svg>
  </div>
</body>
</html>
```